Clever & creative business card needed for a pediatric dentist.

We need a business card for a pediatric dentist that is building a brand-new pediatric dental practice. He is funny, outgoing, and sociable, and he hopes to give his business card to dentists and pediatricians so that he can give them information of where to refer infants, children, and teenagers that need high quality and attainable dental care.

The name of the dental practice is Amber Creek Pediatric Dentistry. Logo design .png / .pdf/ .jpg are provided to aid in the design.

The dentist's last name is Moffat (which sounds like "burger", as in "hamburger” or “cheeseburger"). Since it is pediatric practice, kudos will be given to designs that implement a little joke into the design - but hopefully in a small or hidden way (such as putting something like a cheeseburger on the back of the card, or hiding it an an abstract way).

Thank you!

Please make a design that incorporates colors. It should be fun! Not too serious. It does not have to follow the color scheme of the logos.

```html
<!DOCTYPE html>
<html lang="en">
<head>
<meta charset="utf-8">
<title>Daniel Moffat, D.M.D. — Amber Creek Pediatric Dentistry</title>
<link rel="stylesheet" href="https://fonts.googleapis.com/css2?family=Kumbh+Sans:wght@300;400;600;700&display=swap">
<style>
  :root {
    --green-deep: #2e9150;
    --green-mid: #67b86d;
    --green-soft: #9bcb8c;
    --green-pale: #c2dfb7;
    --green-faint: #eef6ea;
    --ink: #333333;
    --paper: #ffffff;
  }
  html, body {
    margin: 0;
    padding: 0;
    width: 1200px;
    height: 720px;
    overflow: hidden;
    background: var(--paper);
  }
  .card {
    position: relative;
    width: 1200px;
    height: 720px;
    background: var(--paper);
    font-family: "Kumbh Sans", sans-serif;
    color: var(--ink);
    overflow: hidden;
  }
  .brand {
    position: absolute;
    left: 90px;
    top: 228px;
    width: 432px;
    text-align: center;
  }
  .brand-dot {
    display: block;
    width: 120px;
    height: 120px;
    margin: 0 auto 24px;
    border-radius: 50%;
    background: var(--green-mid);
  }
  .brand-name,
  .brand-sub {
    margin: 0;
    font-weight: 600;
    color: var(--ink);
    line-height: 1;
  }
  .brand-name {
    font-size: 56px;
    letter-spacing: 0.5px;
  }
  .brand-sub {
    margin-top: 14px;
    font-size: 19px;
    letter-spacing: 4.6px;
  }
  .divider {
    position: absolute;
    left: 547px;
    top: 171px;
    width: 3px;
    height: 373px;
    background: var(--ink);
  }
  .name-decor {
    position: absolute;
    left: 802px;
    top: 107px;
    width: 128px;
    height: 120px;
    border-radius: 6px;
    background: var(--green-faint);
  }
  .person {
    position: absolute;
    left: 611px;
    top: 166px;
  }
  .person-name {
    margin: 0;
    font-size: 40px;
    font-weight: 700;
    color: var(--green-deep);
    letter-spacing: 0.3px;
    line-height: 44px;
  }
  .person-title {
    margin: 33px 0 0;
    font-size: 26px;
    font-weight: 300;
    font-style: italic;
    line-height: 31px;
  }
  .contact {
    position: absolute;
    left: 611px;
    top: 322px;
    margin: 0;
    padding: 0;
    list-style: none;
    font-size: 29px;
    font-weight: 400;
    line-height: 47px;
  }
  .contact li {
    display: flex;
    align-items: flex-start;
  }
  .contact svg {
    width: 32px;
    height: 47px;
    margin-right: 31px;
    flex: none;
    fill: var(--green-deep);
  }
  .address span { display: block; }
  .color-bar {
    position: absolute;
    left: 0;
    bottom: 0;
    width: 1200px;
    height: 61px;
    display: flex;
  }
  .color-bar span { height: 100%; }
  .bar-deep { width: 317px; background: var(--green-deep); }
  .bar-mid { width: 283px; background: var(--green-mid); }
  .bar-soft { width: 283px; background: var(--green-soft); }
  .bar-pale { width: 317px; background: var(--green-pale); }
</style>
</head>
<body>
<main class="card">
  <section class="brand">
    <span class="brand-dot"></span>
    <p class="brand-name">amber creek</p>
    <p class="brand-sub">PEDIATRIC DENTISTRY</p>
  </section>

  <div class="divider"></div>

  <div class="name-decor" role="img" aria-label="Faint decorative illustration behind the dentist's name"></div>

  <section class="person">
    <h1 class="person-name">DANIEL MOFFAT, D.M.D.</h1>
    <p class="person-title">Board-Certified Pediatric Dentist</p>
  </section>

  <ul class="contact">
    <li>
      <svg viewBox="0 0 32 47" aria-hidden="true"><path d="M7 12c2-1 3-1 4 1l3 5c1 2 0 3-1 4l-2 1c1 4 4 7 8 9l1-2c1-1 2-2 4-1l5 3c2 1 2 2 1 4-1 3-4 5-7 4C12 38 5 30 4 19c0-3 1-6 3-7z"/><path d="M19 9a10 10 0 0 1 9 9h-2a8 8 0 0 0-7-7z M19 14a5 5 0 0 1 4 4h-2a3 3 0 0 0-2-2z"/></svg>
      <span>(555) 014-2600</span>
    </li>
    <li>
      <svg viewBox="0 0 32 47" aria-hidden="true"><path d="M9 9h14v8H9z M2 18h28v12h-5v-4H7v4H2z M8 28h16v10H8z"/></svg>
      <span>(555) 014-2610</span>
    </li>
    <li>
      <svg viewBox="0 0 32 47" aria-hidden="true"><path d="M1 13h30v22H1z" /><path d="M3 15l13 10 13-10" fill="none" stroke="#fff" stroke-width="2"/></svg>
      <span>hello@ambercreekdentistry.com</span>
    </li>
    <li class="address">
      <svg viewBox="0 0 32 47" aria-hidden="true"><path d="M16 8a9 9 0 0 0-9 9c0 7 9 17 9 17s9-10 9-17a9 9 0 0 0-9-9zm0 13a4 4 0 1 1 0-8 4 4 0 0 1 0 8z"/></svg>
      <div>
        <span>48 Meadowlark Lane, Suite 210</span>
        <span>Fairhaven, CT 06500</span>
      </div>
    </li>
  </ul>

  <div class="color-bar">
    <span class="bar-deep"></span>
    <span class="bar-mid"></span>
    <span class="bar-soft"></span>
    <span class="bar-pale"></span>
  </div>
</main>
</body>
</html>
```